" Venda de planos de assistência familiar oferecendo uma rede descontos e funerais para os seus associados ; Serviços funerários; Venda de coroa de flores e arranjos. "

```html
<!DOCTYPE html>
<html lang="pt-BR">
<head>
<meta charset="UTF-8">
<title>Laço Sereno — Papel Timbrado</title>
<link rel="stylesheet" href="https://fonts.googleapis.com/css2?family=Montserrat:wght@500;700&display=swap">
<style>
  :root {
    --canvas-bg: #e9e7e4;
    --paper: #ffffff;
    --teal: #1fa39a;
    --teal-dark: #17837c;
    --ink: #3d4a4a;
    --rule: #2a9d94;
    --faint: #efefef;
  }
  * { margin: 0; padding: 0; box-sizing: border-box; }
  html, body {
    width: 1200px; height: 1200px; overflow: hidden;
    background: var(--canvas-bg);
    font-family: "Montserrat", sans-serif;
  }
  .letterhead {
    position: absolute;
    left: 218px; top: 62px;
    width: 764px; height: 1076px;
    background: var(--paper);
    box-shadow: 0 4px 18px rgba(0,0,0,0.12);
  }
  .brand {
    position: absolute; left: 36px; top: 44px;
    display: flex; align-items: center; gap: 12px;
  }
  .brand-dot {
    width: 34px; height: 34px; border-radius: 50%;
    border: 0; background: var(--teal);
  }
  .brand-name {
    font-weight: 700; font-size: 24px; letter-spacing: 0.5px;
    color: var(--ink); line-height: 1;
  }
  .brand-tagline {
    display: block; margin-top: 6px;
    font-weight: 500; font-size: 8px; letter-spacing: 0.6px;
    color: var(--teal); text-transform: uppercase;
  }
  .header-rule {
    position: absolute; left: 31px; right: 44px; top: 122px;
    height: 2px; background: var(--rule);
  }
  .header-rule::before {
    content: ""; position: absolute; left: 0; top: -2px;
    width: 140px; height: 6px; background: var(--teal);
  }
  .backdrop-mark {
    position: absolute; left: 140px; top: 310px;
    width: 470px; height: 420px; border-radius: 50%;
    background: radial-gradient(circle, var(--faint) 0%, rgba(239,239,239,0.4) 55%, rgba(255,255,255,0) 72%);
  }
  .footer-rule {
    position: absolute; left: 31px; right: 44px; top: 1003px;
    height: 2px; background: var(--rule);
  }
  .footer-rule::after {
    content: ""; position: absolute; right: 0; top: -2px;
    width: 137px; height: 6px; background: var(--teal);
  }
  .contact-row {
    position: absolute; top: 1026px; left: 48px; right: 44px;
    height: 24px;
    font-size: 15px; font-weight: 500; color: var(--teal-dark);
  }
  .contact-item {
    position: absolute; top: 0; display: flex; align-items: center; gap: 10px;
    white-space: nowrap; height: 24px;
  }
  .contact-phone { left: 0; }
  .contact-email { left: 278px; }
  .contact-social { left: 547px; }
  .contact-item svg { flex: none; }
  .social-dot {
    width: 18px; height: 18px; border-radius: 50%;
    border: 2px solid var(--teal);
  }
</style>
</head>
<body>
  <main class="letterhead">
    <header class="brand">
      <span class="brand-dot"></span>
      <div>
        <span class="brand-name">LAÇO SERENO</span>
        <span class="brand-tagline">assistência familiar e funerária</span>
      </div>
    </header>
    <div class="header-rule"></div>

    <div class="backdrop-mark" role="img" aria-label="Marca d'água suave da empresa ao centro da folha"></div>

    <footer>
      <div class="footer-rule"></div>
      <div class="contact-row">
        <div class="contact-item contact-phone">
          <svg width="18" height="18" viewBox="0 0 24 24" fill="none" stroke="var(--teal)" stroke-width="2.4" stroke-linecap="round">
            <path d="M5 3c-2 2-2 6 2 11s9 7 11 5l1.5-1.5-3.5-3-2 1.5c-2-1-4-3-5-5l1.5-2-3-3.5z"/>
          </svg>
          <span>00 0000-0000 | 00 00000-0000</span>
        </div>
        <div class="contact-item contact-email">
          <svg width="22" height="16" viewBox="0 0 22 16" fill="none" stroke="var(--teal)" stroke-width="1.6">
            <rect x="1" y="1" width="20" height="14"/>
            <path d="M1 1l10 8 10-8"/>
          </svg>
          <span>seuemail@seuemail.com.br</span>
        </div>
        <div class="contact-item contact-social">
          <span class="social-dot"></span>
          <span>lacosereno</span>
        </div>
      </div>
    </footer>
  </main>
</body>
</html>
```